Business Card Design Project

Business Card
We are rebranding with a new logo
Industry/Entity Type
Business
Contact Information for Business Card
Doug Farrow +61 457820913 doug@lumora.com.au P.O. Box 728 Kelmscott QLD 4309
Requirements
Must have
- Logo

```html
<!DOCTYPE html>
<html lang="en">
<head>
<meta charset="utf-8">
<title>Lumora International – Business Card</title>
<link rel="stylesheet" href="https://fonts.googleapis.com/css2?family=Open+Sans:wght@400;600;700&display=swap">
<style>
  :root {
    --backdrop: #2b2a2a;
    --card-white: #ffffff;
    --brand-blue: #0d86b8;
    --brand-blue-dark: #0a5f8f;
    --accent-orange: #f0641e;
    --ink: #1d1d1f;
  }
  * { box-sizing: border-box; margin: 0; padding: 0; }
  html, body {
    width: 1200px; height: 716px; overflow: hidden;
    background: var(--backdrop);
    font-family: "Open Sans", sans-serif;
  }
  .stage {
    width: 1200px; height: 716px;
    display: flex; align-items: center; justify-content: center;
  }
  .business-card {
    position: relative;
    width: 900px; height: 514px;
    background: var(--card-white);
    overflow: hidden;
  }
  .card-bands { position: absolute; inset: 0; width: 100%; height: 100%; }
  .brand-lockup { position: absolute; left: 96px; top: 70px; }
  .brand-name {
    font-size: 64px; font-weight: 700; line-height: 1;
    color: var(--brand-blue); letter-spacing: -1px;
  }
  .brand-descriptor {
    margin-top: 8px;
    font-size: 22px; font-weight: 700;
    color: var(--ink); letter-spacing: 6px;
  }
  .contact-block { position: absolute; left: 96px; top: 228px; }
  .contact-name {
    font-size: 21px; font-weight: 600; color: var(--ink);
    padding-bottom: 4px;
    border-bottom: 2px solid var(--brand-blue);
    width: 190px;
  }
  .contact-line {
    display: flex; align-items: center; gap: 8px;
    font-size: 15px; color: var(--ink); margin-top: 6px;
  }
  .contact-line:first-of-type { margin-top: 8px; }
  .contact-icon { width: 14px; height: 14px; flex: none; }
  .postal-address {
    position: absolute; right: 60px; bottom: 118px;
    display: flex; align-items: center; gap: 8px;
    font-size: 17px; font-weight: 600; color: var(--ink);
  }
</style>
</head>
<body>
<main class="stage">
  <article class="business-card">
    <svg class="card-bands" viewBox="0 0 900 514" preserveAspectRatio="none" aria-hidden="true">
      <path d="M0,0 H900 V34 C700,22 350,8 0,6 Z" fill="var(--brand-blue)"/>
      <path d="M0,8 C350,10 700,24 900,36" fill="none" stroke="var(--accent-orange)" stroke-width="2.5"/>
      <path d="M0,296 C200,312 330,452 560,482 C720,500 840,494 900,490 V514 H0 Z" fill="var(--brand-blue)"/>
      <path d="M0,288 C200,302 330,444 560,474 C720,492 840,486 900,482" fill="none" stroke="var(--accent-orange)" stroke-width="4"/>
    </svg>

    <div class="brand-lockup">
      <div class="brand-name">Lumora</div>
      <div class="brand-descriptor">INTERNATIONAL</div>
    </div>

    <div class="contact-block">
      <div class="contact-name">Doug Farrow</div>
      <div class="contact-line">
        <svg class="contact-icon" viewBox="0 0 16 16" aria-hidden="true"><path d="M4 1 L6.5 4.5 L5 6.5 C6 8.5 7.5 10 9.5 11 L11.5 9.5 L15 12 L13 15 C7 14.5 1.5 9 1 3 Z" fill="var(--brand-blue)"/></svg>
        <span>+61 457820913</span>
      </div>
      <div class="contact-line">
        <svg class="contact-icon" viewBox="0 0 16 16" aria-hidden="true"><rect x="1" y="3" width="14" height="10" fill="none" stroke="var(--brand-blue)" stroke-width="1.5"/><path d="M1 3 L8 9 L15 3" fill="none" stroke="var(--brand-blue)" stroke-width="1.5"/></svg>
        <span>doug@lumora.com.au</span>
      </div>
    </div>

    <div class="postal-address">
      <svg class="contact-icon" viewBox="0 0 16 16" aria-hidden="true"><path d="M8 1 C4.7 1 3 3.4 3 5.8 C3 9.5 8 15 8 15 C8 15 13 9.5 13 5.8 C13 3.4 11.3 1 8 1 Z" fill="var(--brand-blue)"/><circle cx="8" cy="6" r="2" fill="var(--card-white)"/></svg>
      <span>P.O. Box 728 Kelmscott QLD 4309</span>
    </div>
  </article>
</main>
</body>
</html>
```